Certified Probate & Trust Postcard

Hi, I am looking for your assistance. I need a postcard design based on the following specifications. The postcard needs to be 6x9. Here are the specifications for the front and back sides. I also need help incorporating a section on the front of the postcard where I can write the name or names of the people I am addressing the postcard to, as well as a space on the back for the stamp and the receiver's address.

(revised 6/18/2025)
🖼️ FRONT SIDE

(Visual: A serene Bay Area home or warm, sunlit interior. Include Tessa’s headshot. Color palette: ivory, slate, soft gold.)

Headline:

You’ve Taken On So Much — Let Me Help with What Comes Next

Subhead:

Strategic Real Estate Guidance for Probate & Trust
Certified Probate & Trust Specialist | Serving the San Francisco Bay Area

⸻

đź“© BACK SIDE

Opening Quote (italicized):

“I lost both of my parents in 2020 — just weeks apart. That experience shaped how I serve every estate I touch.”

⸻

Main Body Copy:

My name is Tessa Harlow, and I’m a Certified Probate & Trust Specialist who works with families, attorneys, and fiduciaries to guide the real estate side of probate with structure, sensitivity, and strategy.

Whether you’re navigating this with legal support or filing in pro per, this process is layered — emotional, procedural, and often overwhelming. I provide a steady hand when everything else feels uncertain.

With over a decade of experience supporting executives at Corvana, Lumidel, and Dunmore Kass, I bring the same operational precision and discretion to every estate I manage. But I also bring empathy — because I’ve been in your shoes.

⸻

What I Offer — At No Upfront Cost to the Estate:
• Property clean-outs, inspections, and basic preparation — coordinated and covered
• Real estate strategy aligned with court timelines and estate goals
• Hands-on collaboration with attorneys or step-by-step guidance for independent petitioners
• Thoughtful communication that honors your time and your grief

Because real estate isn’t just business.
For you, it’s personal. For me, it’s both.

⸻

Call to Action (in soft gold frame or slate border):

If you’re managing a probate or trust estate and need support you can trust — let’s make this easier, together.
Snapgram: @itstessavoy | CareerNet: profilehub.example/in/tessahomeguide

Industry/Entity Type

Real Estate

Requirements
Must have
• Image needs to have a calm aesthetic (remember the person receiving is grieving) emphasis on luxury as we are looking to attract high end clients so not generic and something that is easily purchased from craftly
Nice to have
• need the following design scheme as it relates to color and font Primary Color Palette: 1. Ecru Stone (Soft Beige/Taupe) – #D7CCC0 • Evokes warmth, trust, and sophistication. 2. Slate Charcoal (Deep Neutral Gray) – #4A4A4A • Represents professionalism, authority, and reliability. Accent Colors: 3. Soft Gold (Understated Elegance) – #C2B280 • Adds a subtle richness without being flashy. 4. Powder White (Clean Background Base) – #FAF9F6 • Used for breathing room, high readability, and elegance. Typography/Callout Highlight Color: 5. Trust Blue (Soft Navy) – #3F4A5F • Often used for headers or key points to add credibility and depth. Tessa Harlow should be in cursive, readable and absolutely beautiful
Should not have
• No yellow, do not use ai on my image,

```html
<!DOCTYPE html>
<html lang="en">
<head>
<meta charset="utf-8">
<title>Probate &amp; Trust Postcard – Tessa Harlow</title>
<link rel="stylesheet" href="https://fonts.googleapis.com/css2?family=Montserrat:wght@400;500;600;700;800;900&family=Great+Vibes&display=swap">
<style>
:root{
  --stage:#b9b9b9;
  --slate:#353535;
  --slate-2:#2b2b2b;
  --gold:#c2b280;
  --gold-deep:#a8965f;
  --ecru:#f1eee6;
  --powder:#faf9f6;
  --navy:#3f4a5f;
  --ink:#2a2a2a;
  --line:#6b6b6b;
}
*{box-sizing:border-box;margin:0;padding:0}
html,body{width:900px;height:1200px;overflow:hidden}
body{background:var(--stage);font-family:"Montserrat",sans-serif;color:var(--ink);position:relative}
.card{position:absolute;left:89px;width:722px;height:482px;background:#fff;overflow:hidden;box-shadow:0 10px 22px rgba(0,0,0,.28)}
.front{top:94px}
.back{top:625px}
.abs{position:absolute}
.slate-texture{background:linear-gradient(135deg,#3b3b3b 0%,#2e2e2e 30%,#3a3a3a 50%,#2c2c2c 75%,#363636 100%)}

/* FRONT */
.hero-panel{left:0;top:0;width:722px;height:171px}
.headline{left:38px;top:34px;color:#fff;line-height:.98;font-size:43px;letter-spacing:.5px}
.headline span{display:block}
.headline .light{font-weight:400}
.headline .heavy{font-weight:900}
.hero-photo{left:387px;top:0;width:310px;height:171px;background:linear-gradient(120deg,#6b3a12 0%,#c96a10 35%,#f0a22a 60%,#a4501a 100%);border-left:3px solid #fff;border-right:3px solid #fff}
.gold-band{left:0;top:171px;width:722px;height:114px;background:var(--gold)}
.subhead{left:38px;top:185px;color:var(--slate)}
.subhead .line1{font-size:17px;font-weight:700;line-height:1}
.subhead .line2{font-size:24px;font-weight:400;line-height:1.1;display:flex;align-items:center;gap:6px}
.subhead .line2 b{font-weight:800}
.next-pill{background:var(--navy);color:#fff;font-weight:800;border-radius:18px;padding:0 11px;font-size:23px;line-height:32px}
.tagline{left:38px;top:244px;border-left:2px solid var(--navy);padding-left:6px;font-size:12px;line-height:15px;color:var(--slate)}
.tagline b{font-weight:700}
.thumb{top:178px;width:101px;height:100px;border:1px solid #fff}
.thumb-1{left:384px;background:linear-gradient(160deg,#4a4440,#2a2725 60%,#6d655e)}
.thumb-2{left:492px;background:linear-gradient(160deg,#d8d3c8,#7e8a6a 50%,#3b3b38)}
.thumb-3{left:599px;background:linear-gradient(160deg,#5d6b3e,#a88c5a 55%,#d9cdb0)}
.headshot{border-radius:50%;border:2px solid var(--navy);background:radial-gradient(circle at 50% 45%,#8a6a55,#3f4a5f 70%)}
.front .headshot{left:40px;top:295px;width:98px;height:98px}
.signature{left:44px;top:396px;font-family:"Great Vibes",cursive;font-size:26px;color:var(--ink)}
.contact{left:39px;top:429px;display:flex;align-items:center;white-space:nowrap}
.contact-label{background:var(--gold);color:var(--slate);font-weight:700;font-size:11px;border-radius:10px;padding:0 10px;line-height:20px;position:relative;z-index:1}
.contact-links{border:1px solid var(--gold);border-radius:10px;margin-left:-6px;padding:0 8px 0 11px;line-height:18px;font-size:7.8px;font-weight:500;display:flex;gap:8px;background:#fff}
.dot{display:inline-block;width:7px;height:7px;border-radius:50%;margin-right:3px;vertical-align:-0.5px}
.dot-social{background:#c45a8a}
.dot-career{background:#3a6fa8}
.brand-panel{left:400px;top:285px;width:283px;height:197px}
.badge{left:33px;width:216px;height:20px;background:var(--gold);border-radius:10px;color:var(--slate);font-weight:700;font-size:10px;display:flex;align-items:center;gap:5px;padding-left:5px}
.badge svg{flex:none}
.badge-1{top:20px}
.badge-2{top:46px}
.brand-mark{left:116px;top:82px;width:50px;height:50px;border:1px solid #e6e1d4;border-radius:50%}
.brand-name{left:0;top:136px;width:283px;text-align:center;color:#f1eee6;font-weight:400;font-size:12.5px;letter-spacing:.5px}
.brand-role{left:0;top:153px;width:283px;text-align:center;color:#f1eee6;font-weight:400;font-size:7px;letter-spacing:3px}

/* BACK */
.story{left:0;top:0;width:405px;height:212px;background:var(--ecru)}
.sidebar{left:42px;top:0;width:65px;height:150px;background:var(--slate)}
.side-name{left:42px;top:37px;width:65px;text-align:center;color:var(--gold);font-weight:800;font-size:13px;line-height:14px}
.side-role{left:42px;top:77px;width:65px;text-align:center;color:#fff;font-size:7.5px;line-height:9.5px;font-weight:500}
.back .headshot{left:40px;top:130px;width:68px;height:68px;border-color:#fff;box-shadow:0 0 0 1px var(--navy)}
.quote{left:128px;top:38px;width:254px;font-size:7.4px;font-weight:700;line-height:9.5px;color:var(--ink);padding-left:22px}
.quote-mark{font-family:Georgia,serif;color:var(--gold);font-size:26px;font-weight:700;line-height:1}
.qm-open{left:126px;top:34px}
.qm-close{left:356px;top:46px}
.body-copy{left:128px;top:74px;width:242px;font-size:7.6px;line-height:9.4px;color:#333;text-align:justify}
.body-copy p+p{margin-top:5px}
.offer{left:0;top:214px;width:405px;height:192px}
.offer-title{left:37px;top:18px;font-size:12px;font-weight:800;color:#fff}
.offer-title span{color:var(--gold)}
.offer-item{width:150px;display:flex;gap:6px;align-items:flex-start;color:#fff;font-size:7.7px;line-height:9.4px}
.offer-icon{flex:none;width:27px;height:27px;border-radius:50%;background:var(--gold);border:2px solid #fff;display:flex;align-items:center;justify-content:center}
.oi-1{left:37px;top:54px}
.oi-2{left:216px;top:54px}
.oi-3{left:37px;top:107px}
.oi-4{left:216px;top:107px}
.divider-v{left:199px;top:52px;width:0;height:88px;border-left:1px dotted #777}
.divider-h{left:37px;top:99px;height:0;border-top:1px dotted #777;width:320px}
.belief{left:39px;top:166px;display:flex;align-items:center;white-space:nowrap}
.belief-a{background:var(--gold);color:var(--slate);font-weight:700;font-size:7.5px;line-height:18px;padding:0 9px;border-radius:9px}
.belief-b{background:#fff;color:var(--ink);font-weight:700;font-size:7.5px;line-height:18px;padding:0 9px;border-radius:9px;margin-left:-3px}
.cta{left:0;top:410px;width:405px;height:44px;background:linear-gradient(90deg,#b09a5c,#d9c88e 45%,#c2b280 70%,#a8965f)}
.cta-text{left:38px;top:8px;width:160px;font-size:7.6px;line-height:9.3px;color:var(--slate)}
.cta-text b{font-weight:700}
.cta-links{left:208px;top:7px;font-size:7.8px;font-weight:600;color:var(--slate);line-height:15px;white-space:nowrap}
.stamp{left:595px;top:38px;width:89px;height:91px;background:#ececec;border-radius:8px}
.address-line{left:430px;width:254px;height:0;border-top:1px solid var(--line)}
.al-1{top:292px}
.al-2{top:328px}
.al-3{top:364px}
</style>
</head>
<body>

<section class="card front" aria-label="Postcard front">
  <div class="abs hero-panel slate-texture"></div>
  <h1 class="abs headline">
    <span class="light">YOU’VE</span>
    <span class="heavy">TAKEN ON</span>
    <span class="light">SO MUCH</span>
  </h1>
  <div class="abs hero-photo" role="img" aria-label="Warm sunlit living room with palm plant and sofa"></div>

  <div class="abs gold-band"></div>
  <div class="abs subhead">
    <div class="line1">Let Me Help with</div>
    <div class="line2">What <b>Comes</b> <span class="next-pill">Next</span></div>
  </div>
  <p class="abs tagline">Strategic <b>Real Estate</b><br><b>Guidance</b> for <b>Probate &amp; Trust</b></p>
  <div class="abs thumb thumb-1" role="img" aria-label="Modern grey living room with pendant lights"></div>
  <div class="abs thumb thumb-2" role="img" aria-label="Bright living room with indoor tree"></div>
  <div class="abs thumb thumb-3" role="img" aria-label="Cream sofa on a sunlit garden terrace"></div>

  <div class="abs headshot" role="img" aria-label="Headshot of Tessa Harlow"></div>
  <div class="abs signature">Tessa Harlow</div>
  <div class="abs contact">
    <span class="contact-label">Contact us</span>
    <span class="contact-links">
      <span><i class="dot dot-social"></i>@itstessavoy</span>
      <span><i class="dot dot-career"></i>profilehub.example/in/tessahomeguide</span>
    </span>
  </div>

  <div class="abs brand-panel slate-texture">
    <div class="abs badge badge-1"><svg width="11" height="11" viewBox="0 0 12 12"><circle cx="6" cy="6" r="5.5" fill="#fff"/><path d="M3.3 6.2l1.8 1.8 3.6-3.7" stroke="#a8965f" stroke-width="1.4" fill="none"/></svg>Certified Probate &amp; Trust Specialist</div>
    <div class="abs badge badge-2"><svg width="11" height="11" viewBox="0 0 12 12"><circle cx="6" cy="6" r="5.5" fill="#fff"/><path d="M3.3 6.2l1.8 1.8 3.6-3.7" stroke="#a8965f" stroke-width="1.4" fill="none"/></svg>Serving the San Francisco Bay Area</div>
    <div class="abs brand-mark"></div>
    <div class="abs brand-name">TESSA N. HARLOW</div>
    <div class="abs brand-role">ESTATE ADVISOR</div>
  </div>
</section>

<section class="card back" aria-label="Postcard back">
  <div class="abs story"></div>
  <div class="abs sidebar"></div>
  <div class="abs side-name">TESSA<br>HARLOW</div>
  <div class="abs side-role">Probate &amp;<br>Trust<br>Specialist</div>
  <div class="abs headshot" role="img" aria-label="Headshot of Tessa Harlow"></div>

  <span class="abs quote-mark qm-open">“</span>
  <p class="abs quote">I lost both of my parents in 2020 — just weeks apart. That experience shaped how I serve every estate I touch.</p>
  <span class="abs quote-mark qm-close">”</span>

  <div class="abs body-copy">
    <p>My name is Tessa Harlow, and I’m a Certified Probate &amp; Trust Specialist who works with families, attorneys, and fiduciaries to guide the real estate side of probate with structure, sensitivity, and strategy.</p>
    <p>Whether you’re navigating this with legal support or filing in pro per, this process is layered — emotional, procedural, and often overwhelming. I provide a steady hand when everything else feels uncertain.</p>
    <p>With over a decade of experience supporting executives at Corvana, Lumidel, and Dunmore Kass, I bring the same operational precision and discretion to every estate I manage. But I also bring empathy — because I’ve been in your shoes.</p>
  </div>

  <div class="abs offer slate-texture">
    <h2 class="abs offer-title"><span>What I Offer —</span> At No Upfront Cost to the Estate</h2>
    <div class="abs divider-v"></div>
    <div class="abs divider-h"></div>
    <div class="abs offer-item oi-1"><span class="offer-icon"><svg width="13" height="13" viewBox="0 0 14 14"><circle cx="6" cy="6" r="4" stroke="#353535" stroke-width="1.5" fill="none"/><path d="M9 9l4 4" stroke="#353535" stroke-width="1.6"/></svg></span><span>Property clean-outs, inspections, and basic preparation — coordinated and covered</span></div>
    <div class="abs offer-item oi-2"><span class="offer-icon"><svg width="13" height="13" viewBox="0 0 14 14"><path d="M2 9l4-4 2 2 4-4M2 12h10" stroke="#353535" stroke-width="1.6" fill="none"/></svg></span><span>Hands-on collaboration with attorneys or step-by-step guidance for independent petitioners</span></div>
    <div class="abs offer-item oi-3"><span class="offer-icon"><svg width="13" height="13" viewBox="0 0 14 14"><circle cx="7" cy="7" r="5.5" stroke="#353535" stroke-width="1.3" fill="none"/><circle cx="7" cy="7" r="2.5" stroke="#353535" stroke-width="1.3" fill="none"/></svg></span><span>Real estate strategy aligned with court timelines and estate goals</span></div>
    <div class="abs offer-item oi-4"><span class="offer-icon"><svg width="13" height="13" viewBox="0 0 14 14"><circle cx="7" cy="7" r="5.5" stroke="#353535" stroke-width="1.3" fill="none"/><path d="M7 4v3.3l2 1.5" stroke="#353535" stroke-width="1.3" fill="none"/></svg></span><span>Thoughtful communication that honors your time and your grief</span></div>
    <div class="abs belief"><span class="belief-a">Because real estate isn’t just business</span><span class="belief-b">For you, it’s personal. For me, it’s both</span></div>
  </div>

  <div class="abs cta">
    <p class="abs cta-text">If you’re managing a probate or trust estate and need support you can trust<br><b>let’s make this easier, together</b></p>
    <div class="abs cta-links">
      <div><i class="dot dot-social"></i>@itstessavoy</div>
      <div><i class="dot dot-career"></i>profilehub.example/in/tessahomeguide</div>
    </div>
  </div>

  <div class="abs stamp" aria-label="Stamp area"></div>
  <div class="abs address-line al-1"></div>
  <div class="abs address-line al-2"></div>
  <div class="abs address-line al-3"></div>
</section>

</body>
</html>
```